Business Card Design for new logo

Business card Design for new logo. Follow colors from logo.
The company has offices in multiple comtries
Want to have some bulltes on the countries and also on the main services

Something like
USA*Dominican Republic*LATAM

Consulting*Healthcare IT*Tranformation

Industry/Entity Type

Information Technology

Contact Information for Business Card

Address, Phones, countries, name and position

Lucan morrel

Founder and CEO

947 Tarrow Ln
Marsden Falls, OR 97381

Lmorrel@quendoxcare.com

www.quendoxcare.com

555-304-6182

555-222-2222

```html
<!DOCTYPE html>
<html lang="en">
<head>
<meta charset="utf-8">
<title>Quendox Care — Business Card</title>
<link href="https://fonts.googleapis.com/css2?family=Roboto:wght@400;500;700;900&display=swap" rel="stylesheet">
<style>
  :root {
    --backdrop: #232325;
    --card: #171718;
    --card-edge: #1f1f21;
    --blue: #2a7bc0;
    --orange: #f5904f;
    --white: #f2f2f2;
    --rule: #d8d8d8;
  }
  * { margin: 0; padding: 0; box-sizing: border-box; }
  html, body { width: 1200px; height: 1200px; overflow: hidden; }
  body {
    background: var(--backdrop);
    font-family: "Roboto", Arial, sans-serif;
    position: relative;
  }
  .card {
    position: absolute;
    left: 150px;
    width: 900px;
    height: 514px;
    border-radius: 22px;
    background: linear-gradient(160deg, var(--card-edge), var(--card));
    overflow: hidden;
    box-shadow: 0 10px 30px rgba(0,0,0,.45);
  }
  .card--back { top: 50px; }
  .card--front { top: 630px; }

  .brand-name {
    color: var(--blue);
    font-weight: 900;
    letter-spacing: 1px;
    white-space: nowrap;
  }
  .brand-tagline {
    color: var(--orange);
    font-weight: 500;
    white-space: nowrap;
  }
  .brand-dot {
    display: inline-block;
    border-radius: 50%;
    background: var(--orange);
  }

  /* back */
  .back-brand {
    position: absolute;
    top: 170px; left: 0; right: 0;
    text-align: center;
  }
  .back-brand .brand-dot { width: 56px; height: 56px; margin-bottom: 18px; }
  .back-brand .brand-name { font-size: 64px; display: block; }
  .back-brand .brand-tagline { font-size: 20px; display: block; margin-top: 6px; }
  .back-url {
    position: absolute;
    bottom: 52px; left: 0; right: 0;
    text-align: center;
    color: var(--orange);
    font-size: 19px;
    letter-spacing: .5px;
  }

  /* front */
  .front-brand {
    position: absolute;
    top: 58px; left: 70px;
  }
  .front-brand .brand-dot { width: 54px; height: 54px; margin: 0 0 14px 160px; }
  .front-brand .brand-name { font-size: 62px; display: block; }
  .front-brand .brand-tagline { font-size: 21px; display: block; margin-top: 4px; }

  .person {
    position: absolute;
    top: 150px; right: 70px;
    text-align: right;
  }
  .person-name { color: var(--blue); font-size: 40px; font-weight: 700; }
  .person-title { color: var(--orange); font-size: 22px; margin-top: 2px; }

  .divider {
    position: absolute;
    top: 300px; left: 70px; right: 70px;
    height: 2px;
    background: var(--rule);
  }

  .contact-list, .address-list {
    position: absolute;
    top: 326px;
    list-style: none;
    color: var(--white);
    font-size: 23px;
    line-height: 32px;
  }
  .contact-list { left: 70px; }
  .address-list { right: 70px; text-align: right; }
  .contact-list li, .address-list li { display: flex; align-items: center; gap: 12px; white-space: nowrap; }
  .address-list li { justify-content: flex-end; }
  .icon { width: 22px; height: 22px; flex: none; }
  .icon-spacer { width: 22px; flex: none; }

  .region-band {
    position: absolute;
    bottom: 0; left: 0; right: 0;
    height: 52px;
    background: var(--blue);
    color: var(--white);
    font-size: 24px;
    font-weight: 500;
    display: flex;
    align-items: center;
    justify-content: center;
    gap: 12px;
  }
  .region-band .sep { color: var(--orange); }
</style>
</head>
<body>

  <section class="card card--back">
    <div class="back-brand">
      <span class="brand-dot"></span>
      <span class="brand-name">Quendox Care</span>
      <span class="brand-tagline">Consulting • Healthcare IT • Tranformation</span>
    </div>
    <div class="back-url">www.quendoxcare.com</div>
  </section>

  <section class="card card--front">
    <div class="front-brand">
      <span class="brand-dot"></span>
      <span class="brand-name">Quendox Care</span>
      <span class="brand-tagline">Consulting • Healthcare IT • Tranformation</span>
    </div>

    <div class="person">
      <div class="person-name">Lucan morrel</div>
      <div class="person-title">Founder and CEO</div>
    </div>

    <div class="divider"></div>

    <ul class="contact-list">
      <li>
        <svg class="icon" viewBox="0 0 24 24" aria-hidden="true"><path fill="var(--blue)" d="M6.6 10.8a15.1 15.1 0 0 0 6.6 6.6l2.2-2.2c.3-.3.7-.4 1-.2 1.1.4 2.3.6 3.6.6.6 0 1 .4 1 1V20c0 .6-.4 1-1 1A17 17 0 0 1 3 4c0-.6.4-1 1-1h3.5c.6 0 1 .4 1 1 0 1.3.2 2.5.6 3.6.1.3 0 .7-.2 1z"/></svg>
        555-304-6182
      </li>
      <li>
        <svg class="icon" viewBox="0 0 24 24" aria-hidden="true"><path fill="var(--blue)" d="M6.6 10.8a15.1 15.1 0 0 0 6.6 6.6l2.2-2.2c.3-.3.7-.4 1-.2 1.1.4 2.3.6 3.6.6.6 0 1 .4 1 1V20c0 .6-.4 1-1 1A17 17 0 0 1 3 4c0-.6.4-1 1-1h3.5c.6 0 1 .4 1 1 0 1.3.2 2.5.6 3.6.1.3 0 .7-.2 1z"/></svg>
        555-222-2222
      </li>
      <li>
        <svg class="icon" viewBox="0 0 24 24" aria-hidden="true"><rect x="2" y="5" width="20" height="14" rx="1" fill="none" stroke="var(--blue)" stroke-width="2"/><path d="M2 6l10 7 10-7" fill="none" stroke="var(--blue)" stroke-width="2"/></svg>
        Lmorrel@quendoxcare.com
      </li>
    </ul>

    <ul class="address-list">
      <li>947 Tarrow Ln <span class="icon-spacer"></span></li>
      <li>Marsden Falls, OR 97381
        <svg class="icon" viewBox="0 0 24 24" aria-hidden="true"><path fill="var(--blue)" d="M12 2a7 7 0 0 0-7 7c0 5 7 13 7 13s7-8 7-13a7 7 0 0 0-7-7zm0 9.5A2.5 2.5 0 1 1 12 6.5a2.5 2.5 0 0 1 0 5z"/></svg>
      </li>
      <li>www.quendoxcare.com
        <svg class="icon" viewBox="0 0 24 24" aria-hidden="true"><g fill="none" stroke="var(--blue)" stroke-width="1.8"><circle cx="12" cy="12" r="9.5"/><ellipse cx="12" cy="12" rx="4" ry="9.5"/><path d="M2.5 12h19M4 7h16M4 17h16"/></g></svg>
      </li>
    </ul>

    <div class="region-band">
      <span>USA</span><span class="sep">•</span><span>Dominican Republic</span><span class="sep">•</span><span>LATAM</span>
    </div>
  </section>

</body>
</html>
```